Business Card Design Project

I need a business card designed for TalePorter, a website which has people share their fictional story ideas with others. The business cards should incorporate the websites's logo, which can be found at www.taleporter-demo.net .

Target Market(s)

These will be primarily used in business development activities, not given to customers. It therefore needs to have a clean, professional appearance, and yet communicate what the company is trying to achieve as a bold startup.

Industry/Entity Type

Business

```html
<!DOCTYPE html>
<html lang="en">
<head>
<meta charset="utf-8">
<title>TalePorter Business Card</title>
<link rel="stylesheet" href="https://fonts.googleapis.com/css2?family=Arimo:ital,wght@0,700;1,700&family=Montserrat:wght@500&display=swap">
<style>
  :root {
    --card-blue: #24456a;
    --band-teal: #0c4a48;
    --band-black: #000000;
    --text-white: #ffffff;
    --url-yellow: #f7f200;
  }
  html, body {
    margin: 0;
    padding: 0;
    width: 1200px;
    height: 725px;
    overflow: hidden;
    background: var(--card-blue);
  }
  .card {
    position: relative;
    width: 1200px;
    height: 725px;
    background: var(--card-blue);
  }
  .binding-strip {
    position: absolute;
    left: 0;
    top: 0;
    width: 205px;
    height: 725px;
    background: linear-gradient(to right,
      var(--band-teal) 0, var(--band-teal) 61px,
      var(--band-black) 61px, var(--band-black) 161px,
      var(--band-teal) 161px, var(--band-teal) 205px);
  }
  .brand-name {
    position: absolute;
    left: 205px;
    right: 0;
    top: 22px;
    margin: 0;
    text-align: center;
    font-family: "Montserrat", sans-serif;
    font-weight: 500;
    font-size: 80px;
    line-height: 1.2;
    letter-spacing: 1px;
    color: var(--text-white);
  }
  .mission {
    position: absolute;
    left: 253px;
    top: 180px;
    margin: 0;
    font-family: "Arimo", sans-serif;
    font-weight: 700;
    font-size: 44px;
    line-height: 59px;
    color: var(--text-white);
  }
  .web-address {
    position: absolute;
    left: 292px;
    top: 645px;
    margin: 0;
    font-family: "Arimo", sans-serif;
    font-weight: 700;
    font-style: italic;
    font-size: 47px;
    line-height: 1;
    color: var(--url-yellow);
  }
</style>
</head>
<body>
  <div class="card">
    <div class="binding-strip" role="img" aria-label="Vertical binding strip with yellow criss-cross lacing over a dark teal and black band"></div>
    <h1 class="brand-name">TalePorter</h1>
    <p class="mission">We seek to build a fun and<br>constructive community that allows<br>people from all walks of life to<br>exercise their imagination and see<br>how their new, original ideas for<br>fiction stories compare to those of<br>other users.</p>
    <p class="web-address">www.taleporter-demo.net</p>
  </div>
</body>
</html>
```